Stationery design for software development / consultancy company

We need stationary design based on company logo.

We are based in London, UK and we are providing integration solutions development / consultancy services for VEQ integration projects across UK.

Our name refers two words - integration and grace - and it shows our clients our main specialization field and key characteristics of our solutions / products. We also would like to be associated with follow words: smart, reliable, unique.

Project delivery should include:
- Powerpoint template (needs to have a Cover Page, Table of Contents, 1-2 sample pages, and a Closing/Summary slide at the end)
- Letterhead A4 (Word template)
- Standard invoice A4 (Word template)
- With Compliments Slips A5 (Word template)
- Business card (adobe illustrator)

Attached is logo in vector (please use logo with white background!) and company details for printed stationery.

highly skilled IT professionals

Software

• Clear background in all A4/A5 documents.
All text should be editable, i.e. I will need sources.
• I would prefer light, web 2.0 style colours, follow are in my main interest:
- combination of light grey and orange
- Logo colours
• Please no watermarks on printed stationary

```html
<!DOCTYPE html>
<html lang="en">
<head>
<meta charset="utf-8">
<title>Fluxora – Presentation Template</title>
<link href="https://fonts.googleapis.com/css2?family=Cabin:wght@400;600;700&display=swap" rel="stylesheet">
<style>
  :root{
    --backdrop:#9b9893;
    --paper:#ffffff;
    --charcoal:#3d3d3f;
    --charcoal-deep:#2b2b2d;
    --ink:#3a3a3a;
    --brand-grey:#4b4b4e;
    --orange:#f7941d;
    --green:#8cc63f;
    --blue:#29a9e0;
    --text-light:#ffffff;
  }
  *{margin:0;padding:0;box-sizing:border-box}
  html,body{width:1200px;height:808px;overflow:hidden;background:var(--backdrop)}
  body{position:relative;font-family:"Cabin",sans-serif;color:var(--ink)}

  .slide{position:absolute;width:470px;height:352px;background:var(--paper);overflow:hidden;box-shadow:0 3px 10px rgba(0,0,0,.35)}
  .slide--cover{left:110px;top:30px}
  .slide--heading-one{left:617px;top:30px}
  .slide--heading-two{left:114px;top:421px}
  .slide--closing{left:618px;top:421px}

  .slide__art{position:absolute;inset:0;width:470px;height:352px}

  .brand{position:absolute;display:flex;align-items:center;gap:6px;font-family:"Cabin",sans-serif;font-weight:600;color:var(--brand-grey);letter-spacing:-.3px}
  .brand__dot{border-radius:50%;background:var(--orange)}
  .brand--large{right:38px;top:34px;font-size:34px}
  .brand--large .brand__dot{width:30px;height:30px}
  .brand--small{right:58px;top:32px;font-size:21px}
  .brand--small .brand__dot{width:19px;height:19px}

  .cover-title{position:absolute;left:28px;top:160px;color:var(--text-light)}
  .cover-title__main{font-size:26px;font-weight:700;line-height:1.1}
  .cover-title__sub{font-size:17px;font-weight:400;line-height:1.2}

  .page-heading{position:absolute;left:58px;top:70px;font-size:19px;font-weight:700;color:var(--orange)}
  .page-body{position:absolute;left:58px;top:99px;width:356px;font-size:8.4px;line-height:12.6px;text-align:justify;color:var(--ink)}
  .page-body p + p{margin-top:12.6px}

  .footer-url{position:absolute;left:28px;bottom:16px;font-size:6.6px;color:var(--text-light)}
  .footer-url strong{font-weight:700}

  .closing-title{position:absolute;left:28px;top:162px;color:var(--text-light)}
  .closing-title__main{font-size:26px;font-weight:700;line-height:1.1}
  .closing-title__sub{font-size:17px;line-height:1.2}

  .contact{position:absolute;left:28px;top:248px;color:var(--text-light)}
  .contact__name{font-size:18px;font-weight:600;line-height:1}
  .contact__address{margin-top:6px;font-size:6.8px;font-weight:700;line-height:9px}
  .contact__lines{margin-top:9px;font-size:6.6px;line-height:9.5px;list-style:none}
  .contact__lines li{display:flex;align-items:center;gap:3px}
  .contact__icon{width:7px;height:7px}
</style>
</head>
<body>

<!-- Cover slide -->
<section class="slide slide--cover">
  <svg class="slide__art" viewBox="0 0 470 352" aria-hidden="true">
    <defs>
      <linearGradient id="darkFillA" x1="0" y1="0" x2="1" y2="1">
        <stop offset="0" stop-color="#2e2e30"/><stop offset="1" stop-color="#48484b"/>
      </linearGradient>
    </defs>
    <path d="M0,18 C60,40 120,72 175,102 C110,80 50,60 0,48 Z" fill="var(--green)"/>
    <path d="M0,62 C130,128 300,150 470,100 L470,352 L0,352 Z" fill="url(#darkFillA)"/>
    <path d="M300,136 C370,130 430,116 470,96 L470,104 C420,124 360,134 300,136 Z" fill="var(--blue)"/>
    <circle cx="370" cy="262" r="88" fill="#ffffff" opacity=".05"/>
  </svg>
  <div class="brand brand--large"><span class="brand__dot"></span>fluxora</div>
  <div class="cover-title">
    <h1 class="cover-title__main">Your Title Goes Here</h1>
    <p class="cover-title__sub">Subtitle Goes Here</p>
  </div>
  <p class="footer-url">www.<strong>fluxora</strong>.co.uk</p>
</section>

<!-- Content slide: Heading 1 -->
<section class="slide slide--heading-one">
  <svg class="slide__art" viewBox="0 0 470 352" aria-hidden="true">
    <circle cx="400" cy="262" r="80" fill="#f0f0f0"/>
    <path d="M0,288 C60,300 120,312 175,322 C110,318 50,308 0,300 Z" fill="var(--green)"/>
    <path d="M0,300 C150,326 330,332 470,318 L470,352 L0,352 Z" fill="var(--charcoal)"/>
    <path d="M300,326 C380,326 430,322 470,316 L470,321 C420,326 360,328 300,326 Z" fill="var(--blue)"/>
  </svg>
  <div class="brand brand--small"><span class="brand__dot"></span>fluxora</div>
  <h2 class="page-heading">Heading 1</h2>
  <div class="page-body">
    <p>Lorem Ipsum is simply dummy text of the printing and typesetting industry. Lorem Ipsum has been the industry's standard dummy text ever since the 1500s, when an unknown printer took a galley of type and scrambled it to make a type specimen book. It has survived not only five centuries, but also the leap into electronic typesetting, remaining essentially unchanged. It was popularised in the 1960s with the release of Letraset sheets containing Lorem Ipsum passages, and more recently with desktop publishing software like Aldus PageMaker including versions of Lorem Ipsum.</p>
    <p>Lorem Ipsum is simply dummy text of the printing and typesetting industry. Lorem Ipsum has been the industry's standard dummy text ever since the 1500s, when an unknown printer took a galley of type and scrambled it to make a type specimen book. It has survived not only five centuries, but also the leap into electronic typesetting, remaining essentially unchanged. It was popularised in the 1960s with the release of Letraset sheets containing Lorem Ipsum passages, and more recently with desktop publishing software like Aldus PageMaker including versions of Lorem Ipsum.</p>
  </div>
  <p class="footer-url">www.<strong>fluxora</strong>.co.uk</p>
</section>

<!-- Content slide: Heading 2 -->
<section class="slide slide--heading-two">
  <svg class="slide__art" viewBox="0 0 470 352" aria-hidden="true">
    <circle cx="400" cy="262" r="80" fill="#f0f0f0"/>
    <path d="M0,288 C60,300 120,312 175,322 C110,318 50,308 0,300 Z" fill="var(--green)"/>
    <path d="M0,300 C150,326 330,332 470,318 L470,352 L0,352 Z" fill="var(--charcoal)"/>
    <path d="M300,326 C380,326 430,322 470,316 L470,321 C420,326 360,328 300,326 Z" fill="var(--blue)"/>
  </svg>
  <div class="brand brand--small"><span class="brand__dot"></span>fluxora</div>
  <h2 class="page-heading">Heading 2</h2>
  <div class="page-body">
    <p>Lorem Ipsum is simply dummy text of the printing and typesetting industry. Lorem Ipsum has been the industry's standard dummy text ever since the 1500s, when an unknown printer took a galley of type and scrambled it to make a type specimen book. It has survived not only five centuries, but also the leap into electronic typesetting, remaining essentially unchanged. It was popularised in the 1960s with the release of Letraset sheets containing Lorem Ipsum passages, and more recently with desktop publishing software like Aldus PageMaker including versions of Lorem Ipsum.</p>
    <p>Lorem Ipsum is simply dummy text of the printing and typesetting industry. Lorem Ipsum has been the industry's standard dummy text ever since the 1500s, when an unknown printer took a galley of type and scrambled it to make a type specimen book. It has survived not only five centuries, but also the leap into electronic typesetting, remaining essentially unchanged. It was popularised in the 1960s with the release of Letraset sheets containing Lorem Ipsum passages, and more recently with desktop publishing software like Aldus PageMaker including versions of Lorem Ipsum.</p>
  </div>
  <p class="footer-url">www.<strong>fluxora</strong>.co.uk</p>
</section>

<!-- Closing slide -->
<section class="slide slide--closing">
  <svg class="slide__art" viewBox="0 0 470 352" aria-hidden="true">
    <defs>
      <linearGradient id="darkFillB" x1="0" y1="0" x2="1" y2="1">
        <stop offset="0" stop-color="#2e2e30"/><stop offset="1" stop-color="#48484b"/>
      </linearGradient>
    </defs>
    <path d="M0,18 C60,40 120,72 175,102 C110,80 50,60 0,48 Z" fill="var(--green)"/>
    <path d="M0,62 C130,128 300,150 470,100 L470,352 L0,352 Z" fill="url(#darkFillB)"/>
    <path d="M300,136 C370,130 430,116 470,96 L470,104 C420,124 360,134 300,136 Z" fill="var(--blue)"/>
    <circle cx="370" cy="262" r="88" fill="#ffffff" opacity=".05"/>
  </svg>
  <div class="brand brand--large"><span class="brand__dot"></span>fluxora</div>
  <div class="closing-title">
    <h2 class="closing-title__main">Thank you very much</h2>
    <p class="closing-title__sub">for your valuable time.</p>
  </div>
  <address class="contact" style="font-style:normal">
    <p class="contact__name">fluxora</p>
    <p class="contact__address">42 Elm Court 118 Lower Kingsway Road<br>London SE9 4QT United Kingdom.</p>
    <ul class="contact__lines">
      <li>
        <svg class="contact__icon" viewBox="0 0 10 10" aria-hidden="true"><path d="M2,1 L4,1 L4.6,3 L3.4,4 C4,5.4 4.8,6.2 6,6.6 L7,5.4 L9,6 L9,8 C5,9 1,5 2,1 Z" fill="var(--blue)"/></svg>
        +44(0)120 555 0148
      </li>
      <li>
        <svg class="contact__icon" viewBox="0 0 10 10" aria-hidden="true"><rect x="1" y="2.5" width="8" height="5.5" fill="var(--orange)"/><path d="M1,2.5 L5,5.5 L9,2.5" stroke="#fff" stroke-width=".8" fill="none"/></svg>
        enquiries@fluxora.co.uk
      </li>
    </ul>
  </address>
  <p class="footer-url">www.<strong>fluxora</strong>.co.uk</p>
</section>

</body>
</html>
```